Web page that shows PC specs & equipment of specific Vidloom/Streamvex gamer (KRDM/Zenith)

We want a website that shows the PC specs and equipment of multiple gamers spread over multiple games. We want to start this project NOT with the home page but with a page about one popular gamer's setup: kestrel. You can find his Vidloom channel here:
https://www.vidloom-example.com/kestrel
And his Streamvex here: https://www.streamvex-example.tv/kestrel

We don't have a logo yet. The site name will be RigShelf (domain rigshelf-example.com). Feel free to create a simple dummy logo to fill the space. The site should have a navigation bar with items: Home, Popular Gear, Gamers, Earn Money and Contact Us. The goal of this project is to only build the kestrel page, which is a subpage of Gamers. NOT the home page.

You can grab this gamer's current hardware setup here:
https://kitlogs-example.net/krdm/kestrel-krdm/
https://creatorgear-example.equipment/kestrel/

Most items will link to Bazarro, if they're available there. We won't be selling things ourselves. Only listing things. Please group the equipment and set up in a few blocks/categories:
PC (all known parts of his computer)
Audio equipment (headphones, microphone, ...)
Peripherals (mouse, keyboard, monitor, ...)
Software (his recording software)
I prefer that you show all this equipment on the page so that the user doesn't have to click through to see everything.

The page can include some elements from kestrel's brand, like his logo and a link to his Streamvex and Vidloom. Because the same design will be used for other gamers too (and for the home page, contact, ... ), please avoid making the page 100% like kestrel's brand.

The whole page should look good, use a design that appeals to online gamers, put focus on his equipment and it should be clear that the user can click through to buy this equipment (on Bazarro).

The design should be mobile friendly/responsive.

Target Market(s)

Online gamers and fans of Streamvex players

Industry/Entity Type

Games

Number of Pages Required

1 page

Font styles to use
Serif
Sans Serif

Colors

Designer to choose colors to be used in the design.

Requirements
Must have
• Navigation area
• A content area with PC setup and equipment, divided in category blocks
• Footer area with dummy content
• Responsive design/mobile friendly
Nice to have
• Nice icons to go with the category blocks (can be stock material, preferably from stockvault-example.com)
• Images that go with the items (PC & equipment). I'm not sure yet whether we want to go with a text list or a detailed list with photos.
• If you want to do more, please design a home page or a page for another gamer as well.

```html
<!DOCTYPE html>
<html lang="en">
<head>
<meta charset="utf-8">
<title>Kestrel's Gaming Setup &amp; Gear</title>
<link rel="stylesheet" href="https://fonts.googleapis.com/css2?family=Poppins:wght@700;800&family=Raleway:ital,wght@0,400;0,500;0,600;0,700;1,400&display=swap">
<style>
:root{
  --ink:#0b0b0d;
  --bar:#161616;
  --card:#141414;
  --line:#3a3a3a;
  --blue:#2d35d8;
  --blue-deep:#1e24a8;
  --navy:#0b0e26;
  --white:#ffffff;
  --muted:#c9c9cf;
  --ghost:rgba(255,255,255,.05);
}
*{box-sizing:border-box;margin:0;padding:0}
html,body{width:1200px;height:3554px;overflow:hidden}
body{background:var(--ink);color:var(--white);font-family:"Raleway",sans-serif;position:relative}
.abs{position:absolute}
a{color:inherit;text-decoration:none}

/* header */
.site-header{position:absolute;left:0;top:0;width:1200px;height:92px;background:var(--bar);z-index:5}
.brand{position:absolute;left:145px;top:26px;font:800 36px/40px "Poppins",sans-serif;letter-spacing:.5px}
.main-nav{position:absolute;left:429px;top:36px;display:flex;gap:20px;font:500 13.5px/20px "Raleway",sans-serif;text-transform:uppercase}
.search-icon{position:absolute;left:903px;top:39px}
.social-chip{position:absolute;top:36px;display:flex;align-items:center;gap:5px;font:600 11px/20px "Raleway",sans-serif}
.social-chip i{display:block;width:12px;height:12px;border-radius:50%}
.cart-btn{position:absolute;left:1022px;top:30px;width:32px;height:32px;border:2px solid var(--white);border-radius:50%;display:flex;align-items:center;justify-content:center}

/* hero */
.hero-photo{position:absolute;left:0;top:92px;width:1200px;height:650px;background:radial-gradient(ellipse at 45% 35%,#7b8a7a 0%,#46523f 35%,#1f2620 75%,#111512 100%)}
.hero-title{position:absolute;left:0;top:348px;width:1200px;text-align:center;font:800 58px/64px "Poppins",sans-serif;text-transform:uppercase;text-shadow:0 3px 10px rgba(0,0,0,.45)}
.play-btn{position:absolute;left:553px;top:521px;width:94px;height:94px;border:6px solid var(--white);border-radius:50%}
.play-btn:after{content:"";position:absolute;left:34px;top:22px;border-left:30px solid var(--white);border-top:19px solid transparent;border-bottom:19px solid transparent}
.curve{position:absolute;left:0;width:1200px}

/* section headings */
.section-title{position:absolute;left:0;width:1200px;text-align:center;font:700 40px/46px "Raleway",sans-serif;text-transform:uppercase;display:flex;justify-content:center;align-items:center;gap:14px}
.section-title:before{content:"";width:44px;height:3px;background:var(--blue)}
.ghost-word{position:absolute;font:700 96px/1 "Raleway",sans-serif;color:var(--ghost);text-transform:uppercase;white-space:nowrap}

/* categories */
.categories-bg{position:absolute;left:0;top:731px;width:1200px;height:560px;background:radial-gradient(ellipse at 50% 40%,#1c1c24 0%,#101014 60%,var(--ink) 100%)}
.category{position:absolute;top:939px;width:182px;text-align:center}
.category-ring{width:182px;height:182px;border-radius:50%;background:#070707;border:5px solid var(--blue);border-left-color:#1a1fa0;display:flex;align-items:center;justify-content:center}
.category-name{margin-top:20px;font:500 20px/24px "Raleway",sans-serif}

/* about */
.about-text{position:absolute;left:145px;top:1436px;width:450px}
.about-text h2{font:600 38px/46px "Raleway",sans-serif;text-transform:uppercase}
.rule{width:42px;height:3px;background:var(--blue);margin:16px 0 26px}
.lead{font:600 14.5px/27px "Raleway",sans-serif}
.body-copy{margin-top:12px;font:400 12.5px/27.5px "Raleway",sans-serif;color:var(--muted)}
.btn-pill{display:inline-block;margin-top:38px;background:var(--blue);padding:0 27px;height:46px;line-height:46px;border-radius:23px;font:700 13.5px/46px "Raleway",sans-serif;text-transform:uppercase}
.portrait{position:absolute;left:624px;top:1408px;width:430px;height:430px;border-radius:50%;border:4px solid var(--white);background:radial-gradient(circle at 60% 40%,#3a5fa8 0%,#1f2d56 45%,#0d1226 100%)}

/* products */
.product{position:absolute;width:227px;height:288px;border:1px solid var(--line);background:var(--card);text-align:center}
.product-shot{margin:22px auto 0;width:150px;height:138px;border-radius:4px}
.product h3{margin-top:18px;font:500 16px/20px "Raleway",sans-serif}
.product p{margin-top:6px;font:400 11px/16px "Raleway",sans-serif;color:var(--muted)}
.cart-small{display:inline-block;margin-top:12px;background:var(--blue);padding:0 16px;height:26px;line-height:26px;font:600 10.5px/26px "Raleway",sans-serif;text-transform:uppercase}
.chev{position:absolute;top:2246px}

/* testimonials */
.avatar{position:absolute;left:533px;top:2706px;width:134px;height:134px;border-radius:50%;border:4px solid var(--white);background:radial-gradient(circle at 50% 40%,#c9d4e6 0%,#7f97c2 55%,#3a5590 100%)}
.quote{position:absolute;left:230px;top:2860px;width:740px;text-align:center;font:italic 400 15px/29px "Raleway",sans-serif}
.author{position:absolute;left:0;top:2970px;width:1200px;text-align:center;font:700 17px/22px "Raleway",sans-serif;text-transform:uppercase}
.stars{position:absolute;left:0;top:3006px;width:1200px;text-align:center;font-size:26px;letter-spacing:5px}
.round-btn{position:absolute;top:3071px;width:38px;height:38px;border:1.5px solid var(--white);border-radius:50%;display:flex;align-items:center;justify-content:center}

/* footer */
.footer-col{position:absolute;top:3272px}
.footer-col h4{font:500 16px/20px "Raleway",sans-serif;text-transform:uppercase;margin-bottom:14px}
.footer-col ul{list-style:none;font:400 12px/22px "Raleway",sans-serif}
.footer-col li:before{content:"»";margin-right:14px}
.contact-row{display:flex;gap:12px;font:400 12px/17px "Raleway",sans-serif;margin-bottom:18px}
.email-field{margin-top:14px;width:226px;height:36px;background:var(--white);color:#333;font:400 12px/36px "Raleway",sans-serif;padding-left:16px}
.btn-square{display:inline-block;margin-top:10px;background:var(--blue);padding:0 12px;height:34px;font:700 13px/34px "Raleway",sans-serif;text-transform:uppercase}
.footer-rule{position:absolute;left:145px;top:3468px;width:910px;height:1px;background:#2a2a2a}
.copyright{position:absolute;left:145px;top:3506px;font:400 13px/18px "Raleway",sans-serif}
.foot-social{position:absolute;top:3498px;display:flex;align-items:center;gap:6px;font:600 12px/20px "Raleway",sans-serif}
.foot-social i{width:14px;height:14px;border:2px solid var(--white);border-radius:50%;display:block}
.partner-name{position:absolute;left:940px;top:3494px;font:700 28px/34px "Raleway",sans-serif}
</style>
</head>
<body>

<header class="site-header">
  <div class="brand">KESTREL</div>
  <nav class="main-nav">
    <a href="#">Home</a><a href="#">Popular Gear</a><a href="#">Gamers</a><a href="#">Earn Money</a><a href="#">Contact Us</a>
  </nav>
  <svg class="search-icon" width="13" height="13" viewBox="0 0 13 13" fill="none" stroke="#fff" stroke-width="2"><circle cx="5.5" cy="5.5" r="4"/><path d="M8.5 8.5 12 12"/></svg>
  <a class="social-chip" style="left:930px" href="#"><i style="background:#e51b22"></i>Vidloom</a>
  <a class="social-chip" style="left:930px;top:52px" href="#"><i style="background:var(--blue)"></i>Streamvex</a>
  <a class="cart-btn" href="#"><svg width="16" height="14" viewBox="0 0 16 14" fill="none" stroke="#fff" stroke-width="1.6"><path d="M1 1h2.5l2 8h8l1.5-6H4.5"/><circle cx="6.5" cy="12" r="1.2" fill="#fff"/><circle cx="12.5" cy="12" r="1.2" fill="#fff"/></svg></a>
</header>

<section>
  <div class="hero-photo" role="img" aria-label="Paintball players in camouflage and masks aiming markers in a misty field"></div>
  <svg class="curve" style="top:620px" width="1200" height="140" viewBox="0 620 1200 140">
    <path d="M0 648 Q560 790 1200 641 L1200 760 L0 760Z" fill="var(--ink)"/>
    <path d="M0 648 Q560 790 1200 641" fill="none" stroke="var(--blue)" stroke-width="4"/>
    <path d="M700 720 Q1000 690 1200 641 L1200 655 Q1000 700 700 726Z" fill="var(--blue)"/>
  </svg>
  <h1 class="hero-title">Kestrel's Gaming<br>Setup &amp; Gear</h1>
  <a class="play-btn" href="#" aria-label="Play video"></a>
</section>

<section>
  <div class="categories-bg" role="img" aria-label="Dimmed in-game lobby screen with characters in the background"></div>
  <div class="ghost-word" style="left:1082px;top:1300px;transform:rotate(-90deg);transform-origin:0 0;font-size:88px">Categories</div>
  <h2 class="section-title" style="top:832px">Categories</h2>

  <div class="category" style="left:145px">
    <div class="category-ring"><svg width="90" height="80" viewBox="0 0 90 80" fill="none" stroke="#fff" stroke-width="3"><rect x="4" y="4" width="82" height="54" rx="3"/><path d="M4 48h82M36 58l-4 14M54 58l4 14M24 74h42M38 24l8-8M44 32l14-14"/></svg></div>
    <div class="category-name">Personel<br>Computer</div>
  </div>
  <div class="category" style="left:387px">
    <div class="category-ring"><svg width="80" height="80" viewBox="0 0 80 80" fill="none" stroke="#fff" stroke-width="3.5"><path d="M10 56V40a30 30 0 0 1 60 0v16"/><rect x="8" y="44" width="14" height="26" rx="6"/><rect x="58" y="44" width="14" height="26" rx="6"/></svg></div>
    <div class="category-name">Audio<br>equipment</div>
  </div>
  <div class="category" style="left:629px">
    <div class="category-ring"><svg width="96" height="84" viewBox="0 0 96 84" fill="none" stroke="#fff" stroke-width="2.5"><rect x="8" y="30" width="22" height="40" rx="11"/><path d="M19 30v12M8 44h22"/><rect x="26" y="44" width="64" height="30" rx="3"/><path d="M32 52h52M32 60h52M32 67h52M40 44v30M50 44v30M60 44v30M70 44v30M80 44v30"/><path d="M52 22a14 14 0 0 1 14 14M52 12a24 24 0 0 1 24 24"/></svg></div>
    <div class="category-name">Peripherals</div>
  </div>
  <div class="category" style="left:872px">
    <div class="category-ring"><svg width="90" height="86" viewBox="0 0 90 86" fill="none" stroke="#fff" stroke-width="2.5"><rect x="4" y="6" width="28" height="20"/><rect x="48" y="6" width="36" height="24"/><path d="M4 20h28M48 24h36M18 26v10h50V30M40 36v8"/><ellipse cx="40" cy="50" rx="14" ry="5"/><path d="M26 50v20c0 3 6 5 14 5s14-2 14-5V50M26 60c0 3 6 5 14 5s14-2 14-5"/><circle cx="66" cy="68" r="7"/><path d="M66 56v4M66 76v4M54 68h4M74 68h4"/></svg></div>
    <div class="category-name">Software</div>
  </div>
</section>

<section>
  <svg class="curve" style="top:1285px" width="1200" height="675" viewBox="0 1285 1200 675">
    <defs><linearGradient id="aboutFill" x1="0" y1="0" x2="1" y2="0"><stop offset="0" stop-color="#0c1030"/><stop offset=".6" stop-color="#0a0c1e"/><stop offset="1" stop-color="#14101a"/></linearGradient></defs>
    <path d="M0 1386 Q600 1200 1200 1386 L1200 1862 Q600 2040 0 1862Z" fill="url(#aboutFill)"/>
    <path d="M0 1386 Q600 1200 1200 1386" fill="none" stroke="var(--blue)" stroke-width="4"/>
    <path d="M0 1380 Q300 1300 520 1292 Q250 1310 0 1372Z" fill="var(--blue)"/>
    <path d="M0 1862 Q600 2040 1200 1862" fill="none" stroke="var(--blue)" stroke-width="4"/>
    <path d="M700 1946 Q1000 1920 1200 1856 L1200 1874 Q1000 1935 700 1952Z" fill="var(--blue)"/>
  </svg>
  <div class="ghost-word" style="left:320px;top:1806px;font-size:84px">About</div>
  <div class="about-text">
    <h2>About Me</h2>
    <div class="rule"></div>
    <p class="lead">Marek “kestrel” Valden was born on June 2, 1994 and is a full-time Streamvex streamer. He is currently focusing on KRDM.</p>
    <p class="body-copy">Sed ut perspiciatis unde omnis iste natus error sit voluptatem accusantium doloremque laudantium, totam rem aperiam, eaque ipsa quae ab illo inventore veritatis et quasi architecto beatae vitae dicta sunt explicabo. Nemo enim ipsam voluptatem quia voluptas sit aspernatur aut odit aut fugit, sed quia consequuntur magni dolores eos qui ratione voluptatem.</p>
    <a class="btn-pill" href="#">Read More</a>
  </div>
  <div class="portrait" role="img" aria-label="Portrait of the streamer wearing a headset and a blue team jersey"></div>
</section>

<section>
  <div class="ghost-word" style="left:1186px;top:2530px;transform:rotate(-90deg);transform-origin:0 0;font-size:88px">Products</div>
  <h2 class="section-title" style="top:2043px">Our Products</h2>
  <svg class="chev" style="left:88px" width="24" height="60" viewBox="0 0 24 60" fill="none" stroke="#fff" stroke-width="2"><path d="M22 2 2 30l20 28"/></svg>
  <svg class="chev" style="left:1088px" width="24" height="60" viewBox="0 0 24 60" fill="none" stroke="#fff" stroke-width="2"><path d="M2 2l20 28L2 58"/></svg>

  <div class="product" style="left:131px;top:2131px">
    <div class="product-shot" role="img" aria-label="Boxed desktop processor" style="width:100px;background:linear-gradient(135deg,#3a1450,#0d0d16)"></div>
    <h3>Product Name</h3><p>Morbi diam mauris viverra in gravid</p><a class="cart-small" href="#">Add to cart</a>
  </div>
  <div class="product" style="left:368px;top:2144px">
    <div class="product-shot" role="img" aria-label="Studio microphone on a mount" style="background:linear-gradient(135deg,#2a2a2a,#0f0f0f)"></div>
    <h3>Product Name</h3><p>Morbi diam mauris viverra in gravid</p><a class="cart-small" href="#">Add to cart</a>
  </div>
  <div class="product" style="left:605px;top:2131px">
    <div class="product-shot" role="img" aria-label="Black gaming mouse" style="width:84px;border-radius:40px;background:linear-gradient(160deg,#3a3a3e,#0c0c0e)"></div>
    <h3>Product Name</h3><p>Morbi diam mauris viverra in gravid</p><a class="cart-small" href="#">Add to cart</a>
  </div>
  <div class="product" style="left:843px;top:2144px">
    <div class="product-shot" role="img" aria-label="Gaming motherboard" style="background:linear-gradient(135deg,#2b2b30,#111116)"></div>
    <h3>Product Name</h3><p>Morbi diam mauris viverra in gravid</p><a class="cart-small" href="#">Add to cart</a>
  </div>
</section>

<section>
  <svg class="curve" style="top:2530px" width="1200" height="680" viewBox="0 2530 1200 680">
    <path d="M0 2610 Q600 2470 1200 2590 L1200 3110 Q600 3280 0 3110Z" fill="#3b3b3f"/>
    <path d="M0 2625 Q600 2480 1200 2610 L1200 3098 Q600 3265 0 3098Z" fill="var(--blue)"/>
  </svg>
  <div class="ghost-word" style="left:275px;top:2730px;font-size:90px;color:rgba(0,0,0,.1)">Testimonials</div>
  <h2 class="section-title" style="top:2618px">Testimonials</h2>
  <div class="avatar" role="img" aria-label="Smiling reviewer in a denim jacket"></div>
  <p class="quote">Sed ut perspiciatis unde omnis iste natus error sit voluptatem accusantium doloremque laudantium, totam rem aperiam, eaque ipsa quae ab illo inventore veritatis et quasi architecto beatae vitae dicta sunt explicabo. Nemo enim ipsam voluptatem quia voluptas sit aspernatur aut odit aut fugit</p>
  <div class="author">- John Doe</div>
  <div class="stars">★★★★★</div>
  <a class="round-btn" style="left:556px" href="#"><svg width="8" height="12" viewBox="0 0 8 12" fill="none" stroke="#fff" stroke-width="2"><path d="M7 1 2 6l5 5"/></svg></a>
  <a class="round-btn" style="left:604px" href="#"><svg width="8" height="12" viewBox="0 0 8 12" fill="none" stroke="#fff" stroke-width="2"><path d="M1 1l5 5-5 5"/></svg></a>
</section>

<footer>
  <div class="ghost-word" style="left:30px;top:3554px;transform:rotate(-90deg);transform-origin:0 0;font-size:80px">Contact</div>
  <div class="footer-col" style="left:164px">
    <h4>Contact Info</h4>
    <div class="contact-row"><svg width="16" height="18" viewBox="0 0 16 18" fill="none" stroke="#fff" stroke-width="1.4"><path d="M8 17s6-6 6-10A6 6 0 0 0 2 7c0 4 6 10 6 10z"/><circle cx="8" cy="7" r="2"/></svg><span>122,Lorem ipsum dolor sit amet<br>consectetur adipiscing</span></div>
    <div class="contact-row"><svg width="16" height="16" viewBox="0 0 16 16" fill="none" stroke="#fff" stroke-width="1.4"><path d="M3 1h3l1.5 4-2 1.5a9 9 0 0 0 4 4L11 8.5l4 1.5v3a2 2 0 0 1-2 2A12 12 0 0 1 1 3a2 2 0 0 1 2-2z"/></svg><span>Phone : 1 888 888 8888</span></div>
    <div class="contact-row"><svg width="16" height="14" viewBox="0 0 16 14" fill="none" stroke="#fff" stroke-width="1.4"><rect x="1" y="2" width="14" height="10"/><path d="M1 2l7 6 7-6"/></svg><span>info@companyname.com</span></div>
  </div>
  <div class="footer-col" style="left:419px">
    <h4>Quick Links</h4>
    <ul><li>Home</li><li>Popular Gear</li><li>Gamers</li><li>Earn Money</li><li>Contact Us</li></ul>
  </div>
  <div class="footer-col" style="left:597px">
    <h4>Other Links</h4>
    <ul><li>Terms and conditions</li><li>Sitemap</li><li>Privacy Policy</li><li>My Account</li><li>Support</li></ul>
  </div>
  <div class="footer-col" style="left:808px">
    <h4>Sign Up Newsletter</h4>
    <p style="font:400 12px/16px 'Raleway',sans-serif">Lorem ipsum dolor sit amet consectetur</p>
    <div class="email-field">Enter Email</div>
    <a class="btn-square" href="#">Subscribe</a>
  </div>
  <div class="footer-rule"></div>
  <div class="copyright">Copyrights © 2019, Companyname. All rights reserved</div>
  <a class="foot-social" style="left:800px" href="#"><i></i>Vidloom</a>
  <a class="foot-social" style="left:880px;top:3520px" href="#"><i></i>Streamvex</a>
  <div class="partner-name" style="left:980px">Bazarro</div>
</footer>

</body>
</html>
```